Construction Company Website Design

I need a Website Design for a Construction Company. I have attached logo and business card design files (a.i) to match styles and text for the website. I will need design for 3 pages:
1. A Home page
2. A secondary page (will be different information pages)
3. A contact page with submision form
Website to look professional and match the 'theme' across all pages, using main colours / reverse colours as per design files. Must be clear it is a construction related website without being over the top. Happy for the construction related details (whether that be images/outlines/backgrounds etc to be fairly subtle and not overbearing on the contect of the pages. It will be the content that will be most important, not the images within.

Content has not yet been fully completed but attached is a site map. Each page will need a space for the insertion of the relevant heading and associated content for that particular page. Example can be used as per attached map. If it is preferable to have content completed for this to be a more succesful project please advise and I will complete and submit.

Target Market(s)

Clients for potential construction projects. These could be a range of people. All would be very professional, well educated and put a substantial expection on the quality of website provided.

Industry/Entity Type

Construction

Number of Pages Required

3 page

Font styles to use
Serif
Sans Serif
Other font styles liked:
• fonts preferable as per design files provided unless designer beleives a different font would suit better

Requirements
Must have
• Colour scheme to match logo and business card files provided. Fonts that match as per provided files. Pages must be consistent with the theme carrying across all pages. All pages must have contact details at the bottom of the page.
• Contents of page 1 - 'Home page': multiple tab options / logo link
• Contents of page 2 - 'Secondary page': Top and side navigation / area for information and/or images.
• Contents of page - 'Contact us page': Top and side navigation / Submission form / area for logos such as linkdin, facebook etc.
Nice to have
• Would be good to have a or some generic construction related images - outlines / shadows / effects etc. These might be background images or outlines related to the relevant industry and are consistent across the pages. Could be outlines of buildings, images of men with hardhats etc etc. Good to see colour scheme as per design files used
Should not have
• No pictures of houses. Generally no photos. If any imagery of people must not show faces/details.

```html
<!DOCTYPE html>
<html lang="en">
<head>
<meta charset="utf-8">
<title>Halden Build — We Connect</title>
<link rel="stylesheet" href="https://fonts.googleapis.com/css2?family=Questrial&family=Roboto:wght@300;400;500&family=Lato:wght@400;700;900&display=swap">
<style>
  :root {
    --brand-blue: #0ea5e9;
    --ink-dark: #1d2630;
    --ink-mid: #3a3f45;
    --white: #ffffff;
    --pale-strip: #e9f3f8;
    --card-bg: rgba(22, 26, 32, 0.86);
    --warm-1: #6b4b33;
    --warm-2: #3a2a22;
  }
  * { margin: 0; padding: 0; box-sizing: border-box; }
  html, body { width: 1200px; height: 1200px; overflow: hidden; }
  body { position: relative; background: var(--ink-dark); font-family: "Roboto", sans-serif; }

  /* ---------- Hero ---------- */
  .hero { position: absolute; left: 0; top: 0; width: 1200px; height: 648px; overflow: hidden; }
  .hero-photo { position: absolute; }
  .hero-photo--cranes { left: 0; top: 0; width: 615px; height: 300px; background: linear-gradient(160deg, #5a5a5a, #2f2f2f 70%); }
  .hero-photo--team { left: 615px; top: 0; width: 585px; height: 300px; background: linear-gradient(200deg, #8a8a8a, #505050 75%); }
  .hero-photo--plans { left: 0; top: 300px; width: 615px; height: 348px; background: linear-gradient(20deg, #2e2e2e, #585858 80%); }
  .hero-photo--site { left: 615px; top: 300px; width: 585px; height: 348px; background: linear-gradient(150deg, #3f3f3f, #2a2a2a 60%, #4a4a4a); }
  .hero-tint { position: absolute; inset: 0; background: rgba(30, 30, 30, 0.35); }

  .hero-brand { position: absolute; left: 0; top: 160px; width: 1200px; text-align: center;
    font-family: "Roboto", sans-serif; font-weight: 300; font-size: 46px; letter-spacing: 7px; color: #d9d9d9; text-transform: uppercase; }
  .hero-title { position: absolute; left: 0; top: 258px; width: 1200px; text-align: center;
    font-family: "Questrial", sans-serif; font-weight: 400; font-size: 56px; color: var(--brand-blue); }
  .hero-subtitle { position: absolute; left: 0; top: 326px; width: 1200px; text-align: center;
    font-family: "Roboto", sans-serif; font-weight: 300; font-size: 25px; color: var(--white); }
  .scroll-cue { position: absolute; left: 570px; top: 530px; width: 60px; text-align: center; }
  .scroll-cue span { display: block; margin-top: 4px; font-size: 9.5px; color: #cfcfcf; }

  /* ---------- Header ---------- */
  .site-header { position: absolute; left: 0; top: 648px; width: 1200px; height: 72px; z-index: 5; }
  .site-header > svg { position: absolute; left: 0; top: 0; }
  .header-brand { position: absolute; left: 22px; top: 34px; line-height: 20px;
    font-family: "Roboto", sans-serif; font-weight: 300; font-size: 19px; letter-spacing: 3px; color: var(--ink-mid); text-transform: uppercase; }
  .contact-strip { position: absolute; left: 776px; top: 3px; display: flex; gap: 20px; font-size: 11px; line-height: 13px; color: var(--ink-dark); }
  .contact-item { display: inline-flex; align-items: center; white-space: nowrap; }
  .contact-item svg { flex: 0 0 auto; display: block; margin-right: 4px; }
  .main-nav { position: absolute; left: 425px; top: 29px; display: flex; align-items: center;
    font-family: "Roboto", sans-serif; font-weight: 500; font-size: 12px; letter-spacing: 2.2px; color: var(--ink-dark); }
  .main-nav a { color: inherit; text-decoration: none; }
  .main-nav .sep { margin: 0 28px; font-weight: 400; }

  /* ---------- Feature ---------- */
  .feature-photo { position: absolute; left: 0; top: 700px; width: 1200px; height: 500px;
    background: linear-gradient(100deg, var(--warm-1) 0%, #5a4a44 35%, #324566 55%, #4a3a33 80%, var(--warm-2) 100%); }
  .feature-shade { position: absolute; left: 0; top: 700px; width: 1200px; height: 500px; background: rgba(20, 18, 18, 0.35); }
  .feature-heading { position: absolute; left: 226px; top: 913px; font-family: "Lato", sans-serif; font-weight: 900;
    font-size: 38px; line-height: 34px; color: var(--white); }
  .feature-rule { position: absolute; left: 434px; top: 934px; width: 90px; height: 3px; background: var(--brand-blue); }
  .feature-copy { position: absolute; left: 228px; top: 1000px; width: 445px; font-family: "Lato", sans-serif;
    font-size: 10.5px; line-height: 14px; color: #f1f1f1; }

  /* ---------- Cards ---------- */
  .card { position: absolute; background: var(--card-bg); border-top: 3px solid var(--brand-blue); color: var(--white); }
  .card h3 { font-family: "Roboto", sans-serif; font-weight: 500; text-transform: uppercase; }
  .card p { font-size: 7.6px; line-height: 10px; color: #bfc5cc; }
  .card .btn { position: absolute; border: 1px solid #cfd4d8; background: #2b3138; color: var(--white);
    font-size: 8px; text-align: center; line-height: 14px; height: 16px; }
  .card--project { left: 216px; top: 1114px; width: 263px; height: 78px; padding: 12px 12px; }
  .card--project h3 { font-size: 11px; margin-bottom: 11px; }
  .card--project p { width: 160px; }
  .card--project .btn { left: 177px; top: 52px; width: 73px; }
  .card--cta { left: 483px; top: 1106px; width: 263px; height: 94px; padding: 10px 12px; text-align: center; }
  .card--cta h3 { font-size: 15.5px; margin-bottom: 7px; }
  .card--cta p { width: 210px; margin: 0 auto; }
  .card--cta .btn { left: 95px; top: 61px; width: 73px; }
  .card--news { left: 750px; top: 1114px; width: 262px; height: 78px; padding: 10px 10px; }
  .card--news h3 { font-size: 10.5px; line-height: 13px; }
  .card--news time { display: block; font-size: 7.5px; margin-top: 3px; color: #e6e6e6; }
  .card--news .dots { position: absolute; left: 10px; top: 53px; display: flex; gap: 3px; }
  .card--news .dots i { width: 6px; height: 6px; background: #8d949b; transform: rotate(45deg); }
  .card--news .dots i:first-child { background: var(--brand-blue); }
  .card--news .btn { left: 175px; top: 50px; width: 73px; }
</style>
</head>
<body>

<section class="hero">
  <div class="hero-photo hero-photo--cranes" role="img" aria-label="Black and white photo of tower cranes and steel framework"></div>
  <div class="hero-photo hero-photo--team" role="img" aria-label="Black and white photo of workers in hard hats reviewing plans"></div>
  <div class="hero-photo hero-photo--plans" role="img" aria-label="Black and white photo of hands marking up technical drawings"></div>
  <div class="hero-photo hero-photo--site" role="img" aria-label="Black and white photo of an excavator on a building site"></div>
  <div class="hero-tint"></div>

  <div class="hero-brand">Halden Build</div>
  <h1 class="hero-title">We Connect</h1>
  <p class="hero-subtitle">People and ideas</p>

  <div class="scroll-cue">
    <svg width="22" height="34" viewBox="0 0 22 34" fill="none" stroke="#d8d8d8" stroke-width="1.2">
      <rect x="1" y="1" width="20" height="32" rx="10"/>
      <line x1="1" y1="12" x2="21" y2="12"/>
      <line x1="11" y1="1" x2="11" y2="12"/>
      <rect x="9.5" y="4" width="3" height="5" rx="1.5"/>
    </svg>
    <span>Scroll Down</span>
  </div>
</section>

<section class="feature">
  <div class="feature-photo" role="img" aria-label="Photo of a builder in a hard hat and a client reviewing plans together"></div>
  <div class="feature-shade"></div>
  <h2 class="feature-heading">Your dream<br>partner</h2>
  <div class="feature-rule"></div>
  <p class="feature-copy">Lorem Ipsum is simply dummy text of the printing and typesetting industry. Lorem Ipsum has been the industry's standard dummy text ever since the 1500s, when an unknown printer took a galley of type and scrambled it to make a type specimen book.</p>

  <article class="card card--project">
    <h3>College Residential Village</h3>
    <p>Lorem Ipsum is simply dummy text of the printing and typesetting industry.when an unknown printer book.</p>
    <a class="btn">View Project</a>
  </article>

  <article class="card card--cta">
    <h3>Connect. Create. Design</h3>
    <p>Lorem Ipsum is simply dummy text of the printing and typesetting industry.</p>
    <a class="btn">Discover</a>
  </article>

  <article class="card card--news">
    <h3>Lorem Ipsum is simply dummy text of the printing</h3>
    <time datetime="2018-06-06">2018-06-06</time>
    <div class="dots"><i></i><i></i><i></i><i></i></div>
    <a class="btn">News</a>
  </article>
</section>

<header class="site-header">
  <svg width="1200" height="72" viewBox="0 0 1200 72">
    <rect x="0" y="0" width="1200" height="54" fill="#0ea5e9"/>
    <polygon points="718,0 1200,0 1200,19 742,19" fill="#e9f3f8"/>
    <polygon points="0,12 128,12 552,72 0,72" fill="#ffffff"/>
  </svg>
  <div class="header-brand">Halden Build</div>
  <div class="contact-strip">
    <span class="contact-item">
      <svg width="9" height="9" viewBox="0 0 24 24" fill="#1d2630"><path d="M6.6 10.8a15 15 0 0 0 6.6 6.6l2.2-2.2a1 1 0 0 1 1-.25 11.4 11.4 0 0 0 3.6.57 1 1 0 0 1 1 1V20a1 1 0 0 1-1 1A17 17 0 0 1 3 4a1 1 0 0 1 1-1h3.5a1 1 0 0 1 1 1c0 1.25.2 2.45.57 3.57a1 1 0 0 1-.25 1z"/></svg>
      <span>(01) 123 456 7892</span>
    </span>
    <span class="contact-item">
      <svg width="10" height="8" viewBox="0 0 20 16" fill="#1d2630"><path fill-rule="evenodd" d="M0 0h20v16H0z M2 2v1l8 5 8-5V2z"/></svg>
      <span>info@example.com</span>
    </span>
  </div>
  <nav class="main-nav">
    <a href="#">Home</a><span class="sep">|</span>
    <a href="#">About Us</a><span class="sep">|</span>
    <a href="#">Projects</a><span class="sep">|</span>
    <a href="#">Services</a><span class="sep">|</span>
    <a href="#">Contact Us</a>
  </nav>
</header>

</body>
</html>
```